Healthy Supplement featuring Moringa products

Need 3 business card options for our reps to order from Cardloom. Our reps will be ordering from Cardloom once we upload them. Attached is our current designs to show what info needs to be on the cards. Our website is www.tkvitality.com
The business cards will be a template for our reps to order from. Most of our reps are Asian & Hispanic. Please look at our website so you can see who we are to get the look and feel what we need.
Target Market(s)
Adults 30 on up. Health oriented people.
Industry/Entity Type
Health And Wellness
Contact Information for Business Card
Name
Title
Phone
Logo
www.tkvitality.com/my/username
Font styles to use
Requirements
Must have
- Please match our website look and colors. A moringa leaf is nice, but am open to something different.
Nice to have
- Healthy looking and warm, not super cold or too modern.
Should not have
- No harsh colors please.

```html
<!DOCTYPE html>
<html lang="en">
<head>
<meta charset="utf-8">
<title>TK Vitality – Business Card</title>
<link href="https://fonts.googleapis.com/css2?family=Tinos&display=swap" rel="stylesheet">
<style>
  :root {
    --backdrop: #ebeceb;
    --paper: #ffffff;
    --leaf-dark: #6aaa0e;
    --leaf-light: #94c91c;
    --accent: #e5801f;
    --ink-light: #ffffff;
  }
  * { margin: 0; padding: 0; box-sizing: border-box; }
  html, body {
    width: 1200px; height: 1173px; overflow: hidden;
    background: var(--backdrop);
    font-family: "Tinos", "Times New Roman", serif;
  }
  .card {
    position: absolute; left: 277px; width: 612px; height: 340px;
  }
  .card-front { top: 240px; background: var(--paper); }
  .card-back { top: 630px; background: var(--leaf-dark); overflow: hidden; }

  .brand {
    position: absolute; left: 0; right: 0; top: 118px;
    display: flex; justify-content: center; align-items: center; gap: 14px;
  }
  .brand-dot {
    width: 58px; height: 58px; border-radius: 50%;
    background: var(--leaf-light); flex: none;
  }
  .brand-name {
    color: var(--leaf-dark);
    font-size: 42px; letter-spacing: 2px; line-height: 1;
  }
  .website {
    position: absolute; left: 0; right: 0; top: 287px;
    text-align: center; color: var(--leaf-dark);
    font-size: 20px; line-height: 1;
  }

  .person-name {
    position: absolute; left: 72px; top: 50px;
    color: var(--ink-light); font-size: 24px; line-height: 1;
  }
  .company {
    position: absolute; left: 72px; top: 178px;
    color: var(--ink-light); font-size: 29px; line-height: 1;
  }
  .contact-list { position: absolute; left: 41px; top: 214px; list-style: none; }
  .contact-item {
    display: flex; align-items: center; height: 24px; margin-bottom: 7.5px;
    color: var(--ink-light); font-size: 20px;
  }
  .contact-icon { width: 24px; height: 24px; margin-right: 7px; flex: none; }
  .foliage {
    position: absolute; right: 0; bottom: 0; width: 150px; height: 240px;
    background: radial-gradient(ellipse 100% 100% at 100% 100%,
      var(--leaf-light) 0%, rgba(148,201,28,0.6) 45%, rgba(148,201,28,0) 100%);
  }
</style>
</head>
<body>
  <section class="card card-front">
    <div class="brand">
      <span class="brand-dot"></span>
      <span class="brand-name">TK VITALITY</span>
    </div>
    <div class="website">www.tkvitality.com</div>
  </section>

  <section class="card card-back">
    <div class="person-name">Name</div>
    <div class="company">TK VITALITY</div>
    <ul class="contact-list">
      <li class="contact-item">
        <svg class="contact-icon" viewBox="0 0 24 24" aria-hidden="true">
          <circle cx="12" cy="12" r="11" fill="var(--accent)" stroke="#fff" stroke-width="1.6"/>
          <path d="M12 5.5a4 4 0 0 0-4 4c0 3 4 8 4 8s4-5 4-8a4 4 0 0 0-4-4z" fill="none" stroke="#fff" stroke-width="1.6"/>
          <circle cx="12" cy="9.5" r="1.5" fill="#fff"/>
        </svg>
        Fairview, California
      </li>
      <li class="contact-item">
        <svg class="contact-icon" viewBox="0 0 24 24" aria-hidden="true">
          <circle cx="12" cy="12" r="11" fill="var(--accent)" stroke="#fff" stroke-width="1.6"/>
          <rect x="6" y="8" width="12" height="8" fill="#fff"/>
          <path d="M6 8l6 4.5L18 8" fill="none" stroke="var(--accent)" stroke-width="1"/>
        </svg>
        info@tkvitality.com
      </li>
      <li class="contact-item">
        <svg class="contact-icon" viewBox="0 0 24 24" aria-hidden="true">
          <circle cx="12" cy="12" r="11" fill="var(--accent)" stroke="#fff" stroke-width="1.6"/>
          <path d="M8.5 6.5l2 2-1.2 1.5a7 7 0 0 0 4.7 4.7l1.5-1.2 2 2-1.5 1.7c-4.5-.5-8.5-4.5-9-9z" fill="#fff"/>
        </svg>
        +1(909) 555-0172
      </li>
    </ul>
    <div class="foliage" role="img" aria-label="Decorative moringa leaf branch in light green"></div>
  </section>
</body>
</html>
```